Maplecrest Counseling and Consulting, LLC

We need a business card and stationary designed for a new therapy practice for Laura Whitcombe. Laura Whitcombe is a Therapist who specializes in Therapy for children dealing with trauma and/or stress. Below are some of her thoughts:
colors can include purple, blue, turquoise and green (does NOT have to be all colors) See attached Logos
Laura Whitcombe, LMHC
Maplecrest Counseling & Counseling Inc.
4382 W. Harbor Parkway
Suite 714
Boca Raton, FL 33912
Phone: 561-730-2254
Fax: 561-730-2255
Email: laura@maplecrestcc-example.com
Website: www.maplecrestcc-example.com

```html
<!DOCTYPE html>
<html lang="en">
<head>
<meta charset="utf-8">
<title>Maplecrest Counseling and Consulting – Business Card</title>
<link rel="stylesheet" href="https://fonts.googleapis.com/css2?family=Open+Sans:wght@400;600&family=Arimo:wght@700&family=Questrial&display=swap">
<style>
  :root {
    --leaf-green: #7aa43a;
    --leaf-green-dark: #5f8a2c;
    --slate-grey: #6d6e71;
    --soft-grey: #a3a3a5;
    --mark-grey: #808083;
    --paper: #ffffff;
  }
  html, body {
    margin: 0;
    padding: 0;
    overflow: hidden;
    background: var(--paper);
  }
  .card {
    position: relative;
    width: 687px;
    height: 1200px;
    background: var(--paper);
    overflow: hidden;
  }
  .brand-mark {
    position: absolute;
    left: 50%;
    top: 80px;
    width: 180px;
    height: 180px;
    margin-left: -90px;
    border-radius: 50%;
    background: var(--mark-grey);
  }
  .brand-name {
    position: absolute;
    left: 0;
    width: 100%;
    text-align: center;
    font-family: "Open Sans", sans-serif;
    font-weight: 400;
    color: var(--leaf-green);
    margin: 0;
  }
  .brand-name__main {
    top: 282px;
    font-size: 84px;
    line-height: 110px;
    letter-spacing: 3px;
  }
  .brand-name__sub {
    top: 398px;
    font-size: 29px;
    line-height: 36px;
  }
  .therapist {
    position: absolute;
    top: 496px;
    left: 0;
    width: 100%;
    text-align: center;
    font-family: "Arimo", sans-serif;
    font-weight: 700;
    font-size: 42px;
    line-height: 50px;
    margin: 0;
    text-shadow: 2px 3px 4px rgba(0,0,0,0.35);
  }
  .therapist__name { color: var(--leaf-green); }
  .therapist__credential { color: var(--slate-grey); }
  .contact {
    position: absolute;
    left: 0;
    width: 100%;
    text-align: center;
    font-family: "Questrial", sans-serif;
    margin: 0;
  }
  .contact--phone {
    top: 584px;
    font-size: 48px;
    line-height: 66px;
    color: var(--slate-grey);
  }
  .contact--email {
    top: 736px;
    font-size: 33px;
    line-height: 44px;
    color: var(--leaf-green);
  }
  .contact--address {
    top: 816px;
    font-size: 36px;
    line-height: 46px;
    color: var(--soft-grey);
    font-style: normal;
  }
  .contact--web {
    top: 980px;
    font-size: 40px;
    line-height: 50px;
    color: var(--leaf-green);
  }
  .footer-wave {
    position: absolute;
    left: 0;
    top: 1040px;
    width: 687px;
    height: 160px;
  }
</style>
</head>
<body>
<main class="card">
  <div class="brand-mark"></div>
  <p class="brand-name brand-name__main">Maplecrest</p>
  <p class="brand-name brand-name__sub">Counseling and Consulting, Inc.</p>

  <h1 class="therapist"><span class="therapist__name">Laura Whitcombe,</span> <span class="therapist__credential">LMHC</span></h1>

  <p class="contact contact--phone">P: 561.730.2254<br>F: 561.730.2255</p>
  <p class="contact contact--email">laura@maplecrestcc-example.com</p>
  <address class="contact contact--address">4382 W. Harbor Parkway<br>Suite 714<br>Boca Raton, FL 33912</address>
  <p class="contact contact--web">www.maplecrestcc-example.com</p>

  <svg class="footer-wave" viewBox="0 0 687 160" aria-hidden="true">
    <defs>
      <linearGradient id="waveGreen" x1="0" y1="0" x2="0" y2="1">
        <stop offset="0" stop-color="var(--leaf-green-dark)"/>
        <stop offset="1" stop-color="var(--leaf-green)"/>
      </linearGradient>
      <linearGradient id="waveShadow" x1="0" y1="0" x2="0" y2="1">
        <stop offset="0" stop-color="#9a9a9c"/>
        <stop offset="1" stop-color="#ffffff"/>
      </linearGradient>
    </defs>
    <path d="M0,66 C140,68 190,118 330,118 C480,118 520,54 687,64 L687,110 C520,104 480,160 330,160 C180,160 140,116 0,112 Z" fill="url(#waveShadow)" opacity="0.7"/>
    <path d="M0,12 C150,8 200,78 330,70 C470,62 500,4 687,30 L687,66 C520,52 480,118 330,118 C185,118 140,64 0,66 Z" fill="url(#waveGreen)"/>
  </svg>
</main>
</body>
</html>
```